Varneck Law Business cards and stationary design project

We are looking for a stationary design for business cards (double sided), 8x10, 5x7, and legal and standard envelopes.

We would like the design to match the logo that we have already.
Color palate preferred is Teal, White, grey and any others that will look good for a professional law firm.

We would like this statement: "RELATIONSHIPS. RESPECT. RESULT" to be on the back of the business cards and maybe on the stationary if it looks good.

Please see link to website for more information: www.varneck-law-example.com

Target Market(s)

Potential clients that need Attorney services.

Industry/Entity Type

Law Firm

Contact Information for Business Card

We would like the front and back to be two different colors. Current business cards are teal front, grey back and are a vertical design. We are open to options with colors.

Font styles to use
Serif

Colors
33a6d7
33b8a4
b9b9b9
5c5c5c

Requirements
Must have
• Logo supplied needs to go on the card and stationary.
• Match website color palate, www.varneck-law-example.com
• Be professional and not too wordy.
• Criminal Law, Civil Litigation, Personal Injury, Restraining Orders need to be on the card.
Nice to have
• RELATIONSHIPS. RESPECT. RESULTS. on the back of the card.
Should not have
• Not be too busy/wordy or too flashy.

```html
<!DOCTYPE html>
<html lang="en">
<head>
<meta charset="utf-8">
<title>Varneck Law – Business Card</title>
<link rel="stylesheet" href="https://fonts.googleapis.com/css2?family=Cinzel:wght@400;600&family=Tinos:wght@400;700&display=swap">
<style>
  :root {
    --page: #e9e9ea;
    --charcoal-top: #4a4a4b;
    --charcoal-bottom: #2f2f30;
    --gold: #c9a650;
    --teal: #0f8b9a;
    --teal-deep: #0a7f8d;
    --teal-band: #1ab3a6;
    --white: #ffffff;
  }
  * { margin: 0; padding: 0; box-sizing: border-box; }
  html, body { width: 1200px; height: 800px; overflow: hidden; }
  body {
    background: var(--page);
    position: relative;
    font-family: "Tinos", "Times New Roman", serif;
    color: var(--white);
  }
  .card {
    position: absolute;
    top: 240px;
    width: 560px;
    height: 320px;
    overflow: hidden;
  }
  /* Back of card */
  .card-back {
    left: 26px;
    background: linear-gradient(160deg, var(--charcoal-top), var(--charcoal-bottom));
  }
  .back-name {
    position: absolute;
    top: 92px;
    width: 100%;
    text-align: center;
    font-family: "Cinzel", "Times New Roman", serif;
    font-weight: 400;
    font-size: 44px;
    letter-spacing: 3px;
    color: var(--white);
  }
  .tagline-band {
    position: absolute;
    left: 0;
    right: 0;
    top: 200px;
    height: 52px;
    border-top: 2px solid var(--gold);
    border-bottom: 2px solid var(--gold);
    display: flex;
    align-items: center;
    justify-content: center;
  }
  .tagline {
    font-family: "Cinzel", "Times New Roman", serif;
    font-weight: 600;
    font-size: 21px;
    letter-spacing: 1.5px;
    color: var(--gold);
  }
  /* Front of card */
  .card-front {
    left: 614px;
    background: var(--teal);
  }
  .front-panel {
    position: absolute;
    left: 0;
    top: 0;
    width: 270px;
    height: 100%;
    background: linear-gradient(90deg, var(--teal) 0%, var(--teal-deep) 100%);
    border-top-right-radius: 0 0;
    box-shadow: 6px 0 18px rgba(0,0,0,0.12);
  }
  .front-name {
    position: absolute;
    left: 34px;
    top: 72px;
    font-family: "Cinzel", "Times New Roman", serif;
    font-weight: 400;
    font-size: 27px;
    letter-spacing: 1.5px;
  }
  .practice-list {
    position: absolute;
    left: 34px;
    top: 140px;
    list-style: none;
    font-weight: 700;
    font-size: 25px;
    line-height: 33px;
  }
  .name-band {
    position: absolute;
    left: 280px;
    top: 46px;
    right: 0;
    height: 64px;
    background: var(--teal-band);
    padding: 9px 0 0 20px;
    box-shadow: 0 4px 10px rgba(0,0,0,0.15);
  }
  .person-name { font-weight: 700; font-size: 26px; line-height: 28px; }
  .person-title { font-weight: 700; font-size: 15px; line-height: 18px; }
  .contact-list {
    position: absolute;
    left: 290px;
    top: 132px;
    list-style: none;
    font-weight: 700;
    font-size: 15px;
    line-height: 20px;
  }
  .contact-list li {
    display: flex;
    align-items: flex-start;
    gap: 8px;
    margin-bottom: 6px;
  }
  .contact-list svg { flex: none; width: 18px; height: 18px; margin-top: 1px; }
</style>
</head>
<body>
  <section class="card card-back">
    <h1 class="back-name">VARNECK LAW</h1>
    <div class="tagline-band">
      <p class="tagline">RELATIONSHIPS | RESPECT | RESULTS</p>
    </div>
  </section>

  <section class="card card-front">
    <div class="front-panel"></div>
    <h2 class="front-name">VARNECK LAW</h2>
    <ul class="practice-list">
      <li>Criminal Law</li>
      <li>Civil Litigation</li>
      <li>Personal Injury</li>
      <li>Restraining Orders</li>
    </ul>

    <div class="name-band">
      <p class="person-name">Dana Varneck</p>
      <p class="person-title">Experienced Trial Lawyer</p>
    </div>

    <ul class="contact-list">
      <li>
        <svg viewBox="0 0 24 24" aria-hidden="true"><path fill="#fff" d="M6.6 10.8a15 15 0 0 0 6.6 6.6l2.2-2.2a1 1 0 0 1 1-.25 11.4 11.4 0 0 0 3.6.57 1 1 0 0 1 1 1V20a1 1 0 0 1-1 1A17 17 0 0 1 3 4a1 1 0 0 1 1-1h3.5a1 1 0 0 1 1 1c0 1.25.2 2.45.57 3.57a1 1 0 0 1-.25 1z"/></svg>
        <span>(555) 014 2278</span>
      </li>
      <li>
        <svg viewBox="0 0 24 24" aria-hidden="true"><rect x="2.5" y="5" width="19" height="14" fill="none" stroke="#fff" stroke-width="2"/><path d="M3 6l9 7 9-7" fill="none" stroke="#fff" stroke-width="2"/></svg>
        <span>post@varneck-law-example.com</span>
      </li>
      <li>
        <svg viewBox="0 0 24 24" aria-hidden="true"><rect x="2.5" y="4" width="19" height="16" fill="none" stroke="#fff" stroke-width="2"/><path d="M3 9h18" stroke="#fff" stroke-width="2"/></svg>
        <span>www.varneck-law-example.com</span>
      </li>
      <li>
        <svg viewBox="0 0 24 24" aria-hidden="true"><path fill="#fff" d="M12 2a7 7 0 0 0-7 7c0 5 7 13 7 13s7-8 7-13a7 7 0 0 0-7-7zm0 9.5A2.5 2.5 0 1 1 12 6.5a2.5 2.5 0 0 1 0 5z"/></svg>
        <span>480 Harbor View Ave. #200<br>Seacliff, CA 90000</span>
      </li>
    </ul>
  </section>
</body>
</html>
```